Bluepeak Comfort HVAC Card

Sale, Install, Maintenance Commercial Vent Hood, Ice Machine & Refrigeration
Air Conditioning Heating & Cooling

Industry/Entity Type

Air Conditioning

Contact Information for Business Card

Bluepeak Comfort
2437 Marisol Ave.
Del Rio Tx, 78852
Ph. (830) 555-0172 Tomas J. Villareal Owner
Ph. (830) 555-0438 Hugo Espinoza Tec.
E-mail. bluepeakcomfort2437@mailnest.example

```html
<!DOCTYPE html>
<html lang="en">
<head>
<meta charset="utf-8">
<title>Bluepeak Comfort Business Card</title>
<link href="https://fonts.googleapis.com/css2?family=Arimo:wght@400;700&display=swap" rel="stylesheet">
<style>
  :root {
    --brand-blue: #3a52a6;
    --brand-red: #d8262a;
    --card-white: #ffffff;
    --backdrop: #e9e9ec;
  }
  html, body {
    margin: 0;
    padding: 0;
    overflow: hidden;
  }
  body {
    width: 1200px;
    height: 800px;
    background: var(--backdrop);
    font-family: "Arimo", Arial, sans-serif;
    display: flex;
    align-items: center;
    justify-content: center;
    gap: 40px;
  }
  .card {
    position: relative;
    width: 540px;
    height: 320px;
    box-shadow: 0 6px 18px rgba(0,0,0,0.18);
    overflow: hidden;
  }

  /* Back side */
  .card-back {
    background: var(--brand-blue);
    color: var(--card-white);
    display: flex;
    flex-direction: column;
    align-items: center;
    justify-content: center;
  }
  .card-back .brand-name {
    font-size: 46px;
    font-weight: 400;
    color: var(--card-white);
    margin: 0 0 26px;
    letter-spacing: -0.5px;
  }
  .service-list {
    list-style: none;
    margin: 0;
    padding: 0;
    text-align: center;
    font-size: 13px;
    text-transform: uppercase;
    line-height: 1.75;
    letter-spacing: 0.3px;
  }
  .service-list .sep {
    color: var(--brand-red);
    padding: 0 3px;
  }

  /* Front side */
  .card-front {
    background: var(--card-white);
    color: var(--brand-blue);
  }
  .contacts {
    position: absolute;
    left: 34px;
    top: 30px;
    font-size: 15px;
  }
  .person-name {
    font-size: 18px;
    font-weight: 700;
    margin: 0;
    color: var(--brand-blue);
  }
  .person-name .surname { color: var(--brand-red); }
  .person-role {
    font-size: 14px;
    margin: 1px 0 10px;
  }
  .contact-line {
    display: flex;
    align-items: center;
    gap: 7px;
    margin: 0 0 20px;
    font-size: 15px;
  }
  .contact-line svg { flex: none; }
  .contact-email { margin-top: 10px; font-size: 14px; }

  .brand-block {
    position: absolute;
    right: 34px;
    top: 128px;
    text-align: left;
  }
  .card-front .brand-name {
    font-size: 34px;
    font-weight: 400;
    color: var(--brand-blue);
    margin: 0;
    letter-spacing: -0.4px;
  }
  .address {
    margin: 4px 0 0;
    font-size: 13px;
    font-weight: 700;
    color: var(--brand-red);
  }
  .finance-note {
    position: absolute;
    right: 40px;
    bottom: 48px;
    margin: 0;
    font-size: 16px;
    font-weight: 700;
    color: var(--brand-red);
  }
  .color-band {
    position: absolute;
    left: 0;
    right: 0;
    bottom: 0;
    height: 30px;
    display: flex;
  }
  .color-band .band-blue { flex: 0 0 56%; background: var(--brand-blue); }
  .color-band .band-gap { flex: 0 0 3px; background: var(--card-white); }
  .color-band .band-red { flex: 1; background: var(--brand-red); }
</style>
</head>
<body>

  <section class="card card-front" aria-label="Business card front">
    <div class="contacts">
      <p class="person-name">Tomas J. <span class="surname">Villareal</span></p>
      <p class="person-role">Owner</p>
      <p class="contact-line">
        <svg width="12" height="14" viewBox="0 0 12 14" aria-hidden="true"><path d="M3 1 L5 4 L3.6 5.6 C4.4 7.6 5.4 9 7 10.2 L8.6 8.9 L11 11.2 L9.4 13 C5 12 1.5 7.5 1 2.6 Z" fill="var(--brand-red)"/></svg>
        <span>(830) 555-0172</span>
      </p>
      <p class="person-name">Hugo <span class="surname">Espinoza</span></p>
      <p class="person-role">Tec.</p>
      <p class="contact-line">
        <svg width="12" height="14" viewBox="0 0 12 14" aria-hidden="true"><path d="M3 1 L5 4 L3.6 5.6 C4.4 7.6 5.4 9 7 10.2 L8.6 8.9 L11 11.2 L9.4 13 C5 12 1.5 7.5 1 2.6 Z" fill="var(--brand-red)"/></svg>
        <span>(830) 555-0438</span>
      </p>
      <p class="contact-line contact-email">
        <svg width="16" height="11" viewBox="0 0 16 11" aria-hidden="true"><rect x="0" y="0" width="16" height="11" fill="var(--brand-red)"/><path d="M0.5 0.5 L8 6 L15.5 0.5" fill="none" stroke="#fff" stroke-width="1.2"/></svg>
        <span>bluepeakcomfort2437@mailnest.example</span>
      </p>
    </div>

    <div class="brand-block">
      <p class="brand-name">Bluepeak Comfort</p>
      <p class="address">2437 Marisol Ave. Del Rio Tx, 78852</p>
    </div>

    <p class="finance-note">100% Finance Available</p>

    <div class="color-band" aria-hidden="true">
      <span class="band-blue"></span><span class="band-gap"></span><span class="band-red"></span>
    </div>
  </section>

  <section class="card card-back" aria-label="Business card back">
    <p class="brand-name">Bluepeak Comfort</p>
    <ul class="service-list">
      <li>Sale<span class="sep">/</span>Install<span class="sep">/</span>Maintenance</li>
      <li>Commercial Vent Hood<span class="sep">/</span>Ice Machine &amp; Refrigeration</li>
      <li>Air Conditioning<span class="sep">/</span>Heating &amp; Cooling</li>
    </ul>
  </section>

</body>
</html>
```